KR Stationary Design

Logo, Business Card, Letterhead & Email Signature Design

Target Market(s)

Legal

Colors

Designer to choose colors to be used in the design.

Requirements
Must have
• Gold and Blue are the colours to use. The KR must be inside the Gold Legal Pendulum

```html
<!DOCTYPE html>
<html lang="en">
<head>
<meta charset="utf-8">
<title>KR Kgosana Stationery</title>
<link rel="stylesheet" href="https://fonts.googleapis.com/css2?family=Montserrat:ital,wght@0,400;0,500;0,600;1,400;1,500&display=swap">
<style>
:root{
  --blue:#21608f;
  --blue-deep:#1d5a87;
  --gold:#c49a3c;
  --gold-light:#e6c66a;
  --ink:#2a2a2a;
  --paper:#ffffff;
  --ground:#e9eaec;
}
*{margin:0;padding:0;box-sizing:border-box}
html,body{width:1195px;height:1200px;overflow:hidden}
body{background:var(--ground);font-family:"Montserrat",Arial,sans-serif;position:relative;color:var(--ink)}
.sheet{position:absolute;background:var(--paper);overflow:hidden}

/* brand lockup */
.brand-pill{position:absolute;background:var(--blue);display:flex;flex-direction:column;align-items:center;justify-content:center}
.brand-pill .arc{position:absolute;left:4px;top:0;height:100%}
.wordmark{color:var(--gold);font-weight:500;text-align:center;line-height:1.05;letter-spacing:.06em}
.wordmark .initials{display:block}
.wordmark .inc{display:block;letter-spacing:.22em}

/* contact list */
.contacts{list-style:none;color:var(--blue)}
.contacts li{display:flex;align-items:center}
.contacts svg{fill:var(--gold);flex:none}

/* letterhead */
.letterhead{left:84px;top:306px;width:454px;height:586px}
.letterhead .brand-pill{left:255px;top:16px;width:199px;height:90px;border-radius:45px 0 0 45px}
.letterhead .wordmark{font-size:13px}
.letterhead .wordmark .initials{font-size:20px;margin-bottom:2px}
.letterhead .wordmark .inc{font-size:6px;margin-top:3px}
.letterhead .contacts{position:absolute;left:39px;top:46px;font-size:7.6px}
.letterhead .contacts li{height:10.6px;gap:5px}
.letter-body{position:absolute;left:39px;top:189px;width:378px;font-size:7.3px;line-height:14.4px}
.letter-body p{margin-bottom:14.4px}
.letter-rule{position:absolute;left:39px;top:541px;width:374px;height:1px;background:linear-gradient(90deg,var(--gold),var(--gold-light),var(--gold))}
.letter-address{position:absolute;left:0;top:553px;width:454px;text-align:center;color:var(--blue);font-size:7.3px}

/* business card front */
.card-front{left:611px;top:500px;width:183px;height:104px}
.card-front .brand-pill{left:91px;top:0;width:92px;height:104px;border-radius:52px 0 0 52px}
.card-front .wordmark{font-size:8px;padding-left:6px}
.card-front .wordmark .initials{font-size:12px}
.card-front .wordmark .inc{font-size:3.6px;margin-top:2px}
.card-name{position:absolute;left:10px;top:20px;color:var(--gold);font-size:6.6px;font-weight:500;letter-spacing:.02em}
.card-role{position:absolute;left:10px;top:28px;color:var(--blue);font-size:4.4px}
.card-address{position:absolute;left:10px;top:40px;color:var(--blue);font-size:4.4px;line-height:5.1px}
.card-front .contacts{position:absolute;left:10px;top:67px;font-size:4.6px}
.card-front .contacts li{height:7.4px;gap:4px}

/* business card back */
.card-back{left:935px;top:500px;width:183px;height:104px;background:var(--blue);display:flex;align-items:center;justify-content:center}
.card-back .wordmark{font-size:10.5px}
.card-back .wordmark .initials{font-size:15px;margin-bottom:2px}
.card-back .wordmark .inc{font-size:4.6px;margin-top:2px;color:var(--gold)}

/* email signature */
.signature{left:611px;top:675px;width:507px;height:217px}
.signature .brand-pill{left:344px;top:8px;width:163px;height:88px;border-radius:44px 0 0 44px}
.signature .wordmark{font-size:12.5px;padding-left:6px}
.signature .wordmark .initials{font-size:19px;margin-bottom:2px}
.signature .wordmark .inc{font-size:5.8px;margin-top:3px}
.sign-off{position:absolute;left:20px;top:18px;font-size:7.4px}
.sign-name{position:absolute;left:20px;top:33px;color:var(--gold);font-size:6.8px;font-weight:500;letter-spacing:.03em}
.signature .contacts{position:absolute;left:20px;top:47px;font-size:6.9px}
.signature .contacts li{height:9.6px;gap:4px}
.sign-address{position:absolute;left:20px;top:79px;color:var(--blue);font-size:6.9px}
.disclaimer{position:absolute;left:20px;top:122px;width:468px;font-size:4.3px;line-height:5.4px;color:var(--ink)}
.disclaimer p{margin-bottom:4.2px}
.disclaimer em{color:var(--blue);font-style:italic;font-weight:500}
.disclaimer .scheme{color:#2a3c8f;font-style:italic;font-size:4.6px;margin-bottom:5px}
.sign-rule{position:absolute;left:20px;top:204px;width:468px;height:1px;background:linear-gradient(90deg,var(--gold),var(--gold-light),var(--gold))}
</style>
</head>
<body>

<svg width="0" height="0" style="position:absolute" aria-hidden="true">
  <defs>
    <linearGradient id="goldArc" x1="0" y1="0" x2="0" y2="1">
      <stop offset="0" stop-color="#c49a3c" stop-opacity="0"/>
      <stop offset=".5" stop-color="#f0d27a"/>
      <stop offset="1" stop-color="#c49a3c" stop-opacity="0"/>
    </linearGradient>
    <symbol id="icon-phone" viewBox="0 0 10 8"><path d="M1 2.5C2 .5 8 .5 9 2.5L8 3.6 6.6 2.9V2.2H3.4v.7L2 3.6zM2.8 4h4.4L8 7.5H2z"/></symbol>
    <symbol id="icon-fax" viewBox="0 0 10 8"><path d="M0 3h5.5V1.5L9.5 4 5.5 6.5V5H0z"/></symbol>
    <symbol id="icon-mail" viewBox="0 0 10 8"><path d="M0 1h10v6H0zM.8 1.6 5 4.6l4.2-3z" fill-rule="evenodd"/></symbol>
  </defs>
</svg>

<!-- Letterhead -->
<section class="sheet letterhead">
  <ul class="contacts">
    <li><svg width="8" height="7"><use href="#icon-phone"/></svg>011 555 0184</li>
    <li><svg width="8" height="7"><use href="#icon-fax"/></svg>086 555 0297</li>
    <li><svg width="8" height="7"><use href="#icon-mail"/></svg>thabo@krkgosana.co.za</li>
  </ul>
  <div class="brand-pill">
    <svg class="arc" viewBox="0 0 10 90" width="10" preserveAspectRatio="none"><path d="M9 12Q1 45 9 78" stroke="url(#goldArc)" stroke-width="1.6" fill="none"/></svg>
    <div class="wordmark"><span class="initials">KR</span>KGOSANA<span class="inc">INCORPORATED</span></div>
  </div>
  <div class="letter-body">
    <p>Sincearly,</p>
    <p>This is a sample letter that has been placed to demonstrate typing remat (Your Company). letterhead design. When positioned properly, it will serve to work in harmony with all other elements letterhead. This letterhead design is meant to project an image</p>
    <p>This letterhead design is meant project an image of professionalism reliability. By using simple aligen we have created a very spacious feeling. The simplicity suggest &nbsp;rengththe spaciousnes contributes haesthetics the layout. These basic qualities along with the (Your Company)</p>
    <p>look and helps reinforce the (Your Company) brand. letterhead design is meant to project an image design. When positioned properly, it will serve to work in harmony all the other elements letterhead. sionalism and reliability.</p>
    <p>This letterhead design is based on the (Form of your logo) form (Your Company) logo. Each stationery we have created a very spacious feeling. The simplicity suggests strength the spaciousnes contribute part of the (Form of your logo).</p>
  </div>
  <div class="letter-rule"></div>
  <p class="letter-address">Block B Fernhill Office Park, 24 Ridgeway road north. Sandton, 2196</p>
</section>

<!-- Business card front -->
<section class="sheet card-front">
  <p class="card-name">THABO KGOSANA</p>
  <p class="card-role">Director</p>
  <p class="card-address">Block B Fernhill Office Park<br>24 Ridgeway road north<br>Sandton, 2196</p>
  <ul class="contacts">
    <li><svg width="5" height="4"><use href="#icon-phone"/></svg>011 555 0184</li>
    <li><svg width="5" height="4"><use href="#icon-fax"/></svg>086 555 0297</li>
    <li><svg width="5" height="4"><use href="#icon-mail"/></svg>thabo@krkgosana.co.za</li>
  </ul>
  <div class="brand-pill">
    <svg class="arc" viewBox="0 0 10 104" width="8" preserveAspectRatio="none"><path d="M9 14Q1 52 9 90" stroke="url(#goldArc)" stroke-width="1.6" fill="none"/></svg>
    <div class="wordmark"><span class="initials">KR</span>KGOSANA<span class="inc">INCORPORATED</span></div>
  </div>
</section>

<!-- Business card back -->
<section class="sheet card-back">
  <div class="wordmark"><span class="initials">KR</span>KGOSANA<span class="inc">INCORPORATED</span></div>
</section>

<!-- Email signature -->
<section class="sheet signature">
  <p class="sign-off">Kindest regards,</p>
  <p class="sign-name">THABO KGOSANA</p>
  <ul class="contacts">
    <li><svg width="7" height="6"><use href="#icon-phone"/></svg>011 555 0184</li>
    <li><svg width="7" height="6"><use href="#icon-fax"/></svg>086 555 0297</li>
    <li><svg width="7" height="6"><use href="#icon-mail"/></svg>thabo@krkgosana.co.za</li>
  </ul>
  <p class="sign-address">Block B Fernhill Office Park, 24 Ridgeway road north. Sandton, 2196</p>
  <div class="brand-pill">
    <svg class="arc" viewBox="0 0 10 88" width="9" preserveAspectRatio="none"><path d="M9 12Q1 44 9 76" stroke="url(#goldArc)" stroke-width="1.6" fill="none"/></svg>
    <div class="wordmark"><span class="initials">KR</span>KGOSANA<span class="inc">INCORPORATED</span></div>
  </div>
  <div class="disclaimer">
    <p><em>Important note:</em> This E-Mail and any attachment is PRIVILEGED and confidential. &nbsp;It must not be read, copied, disclosed or used by any person other than the above named addressees. In order to preserve the intended confidentiality and privilege, please notify us immediately if you have received this e-mail by mistake and secure-delete this e-mail from your system. Unauthorised perusal, use, disclosure, forwarding or copying is strictly prohibited and may be unlawful.</p>
    <p class="scheme">Liability limited by a scheme approved under Professional Standards Legislation. Legal practitioners at Harbourlaw Pty Ltd are members of the scheme.</p>
    <p><em>Fraud warning:</em> Please be aware that there is a significant risk posed by cyber fraud, specifically relating to email accounts and bank account details. Our bank account details will never change during the course of a transaction, and we will never advise you of a change to our bank details via email. &nbsp;Please check account details with us in person or by phone before making payments. If you advise us of your bank account details by email, please also ring and confirm the bank account details by phone as well.</p>
  </div>
  <div class="sign-rule"></div>
</section>

</body>
</html>
```